Brinmoor Logistics - Cards and Logo

We need a logo and card design for a Logistics company located in Chicago. Our competitors are KRV and Torvan. We would like to see designs that incorporate a logo that shows all ways in terms of direction. The colors would be Electric Blue, Grays, Blacks and White. I like how Pumo has a badge type logo that is strong and clean. Quorvel also has a strong font that is futuristic. The final design should communicate we are a strong and technological type of company. I show a picture of the colors we like from a pumo cooler.

```html
<!DOCTYPE html>
<html lang="en">
<head>
<meta charset="utf-8">
<title>Brinmoor Logistics – Business Cards</title>
<link href="https://fonts.googleapis.com/css2?family=Open+Sans:wght@400;600;800&display=swap" rel="stylesheet">
<style>
  :root {
    --navy: #07356b;
    --gray: #8a8a8a;
    --ring: #7d7d7d;
    --white: #ffffff;
    --backdrop: #d9d9d9;
  }
  * { margin: 0; padding: 0; box-sizing: border-box; }
  html, body {
    width: 1200px; height: 900px; overflow: hidden;
    background: var(--backdrop);
    font-family: "Open Sans", Arial, sans-serif;
  }
  .card {
    position: absolute;
    width: 560px; height: 320px;
    border-radius: 26px;
    overflow: hidden;
    box-shadow: 0 6px 14px rgba(0,0,0,0.18);
  }
  /* Front */
  .card-front {
    left: 110px; top: 120px;
    background: var(--navy);
    display: flex; align-items: center; justify-content: center; gap: 18px;
  }
  .front-badge {
    width: 54px; height: 54px; border-radius: 50%;
    border: 4px solid var(--white);
  }
  .wordmark {
    font-weight: 800; text-transform: uppercase; line-height: 0.95;
    letter-spacing: 1px;
  }
  .card-front .wordmark { color: var(--white); font-size: 40px; }
  .wordmark .line-two { letter-spacing: 9px; font-size: 0.72em; display: block; }

  /* Back */
  .card-back { left: 530px; top: 470px; background: var(--white); }
  .back-band { position: absolute; inset: 0; }
  .card-back .wordmark {
    position: absolute; right: 34px; top: 28px;
    color: var(--navy); font-size: 36px; text-align: right;
  }
  .contact {
    position: absolute; right: 34px; top: 138px;
    color: var(--white); text-align: right;
  }
  .contact-name { font-size: 19px; font-weight: 600; letter-spacing: 0.5px; line-height: 1.1; }
  .contact-role { font-size: 14px; margin-bottom: 10px; }
  .contact-line {
    font-size: 14px; line-height: 1.4;
    display: flex; justify-content: flex-end; align-items: center; gap: 6px;
  }
  .contact-line svg { width: 12px; height: 12px; flex: none; }
</style>
</head>
<body>

<section class="card card-front" aria-label="Card front">
  <span class="front-badge"></span>
  <div class="wordmark">Brinmoor<span class="line-two">Logistics</span></div>
</section>

<section class="card card-back" aria-label="Card back">
  <svg class="back-band" viewBox="0 0 560 320" width="560" height="320">
    <polygon points="250,120 560,120 560,265 175,265" fill="var(--navy)"/>
    <circle cx="120" cy="232" r="86" fill="none" stroke="var(--ring)" stroke-width="9"/>
  </svg>

  <div class="wordmark">Brinmoor<span class="line-two">Logistics</span></div>

  <div class="contact">
    <div class="contact-name">DANIEL CRANE</div>
    <div class="contact-role">Managing Director</div>
    <div class="contact-line">044-555 0142 876
      <svg viewBox="0 0 12 12"><path d="M2 1h3l1 3-1.5 1a6 6 0 0 0 2.5 2.5L8 6l3 1v3a1 1 0 0 1-1 1A9 9 0 0 1 1 2a1 1 0 0 1 1-1z" fill="#fff"/></svg>
    </div>
    <div class="contact-line">044-555 0142 876
      <svg viewBox="0 0 12 12"><rect x="3" y="0.5" width="6" height="11" rx="1" fill="none" stroke="#fff" stroke-width="1.2"/><circle cx="6" cy="9.5" r="0.8" fill="#fff"/></svg>
    </div>
    <div class="contact-line">info@brinmoor.com
      <svg viewBox="0 0 12 12"><rect x="0.5" y="2" width="11" height="8" fill="#fff"/><path d="M0.5 2l5.5 4.5L11.5 2" fill="none" stroke="var(--navy)" stroke-width="1"/></svg>
    </div>
    <div class="contact-line">www.brinmoorlogistics.com
      <svg viewBox="0 0 12 12"><circle cx="6" cy="6" r="5.5" fill="#fff"/><path d="M0.5 6h11M6 0.5c-3 3-3 8 0 11M6 0.5c3 3 3 8 0 11" fill="none" stroke="var(--navy)" stroke-width="0.8"/></svg>
    </div>
  </div>
</section>

</body>
</html>
```